Brochure Design Project

I need a presentation folder with two inside pages and a pocket on back cover, use use my logo ,
make the cover just using the logo (put it big and centered, then use the logo in the background to fill, read the brief and make it modern, stop trying to make it exactly like the picture I gave as sample please use your talent trust your self
I just uploaded text for presentation folder
Dr's offices and patients

```html
<!DOCTYPE html>
<html lang="en">
<head>
<meta charset="utf-8">
<title>Northvale Counseling – Presentation Folder Inside Spread</title>
<link rel="stylesheet" href="https://fonts.googleapis.com/css2?family=Didact+Gothic&display=swap">
<style>
  :root {
    --folder-brown: #5b3a22;
    --folder-deep: #4a2e1a;
    --pocket-brown: #8a4a2b;
    --sepia-light: #c9a886;
    --sepia-mid: #a27a57;
    --sepia-dark: #6e4a2e;
    --paper: #ece8df;
    --ink: #2a2220;
    --brand: #8a4a2b;
  }
  * { margin: 0; padding: 0; box-sizing: border-box; }
  html, body { width: 1200px; height: 801px; overflow: hidden; background: var(--folder-brown); }
  .spread {
    position: relative; width: 1200px; height: 801px; overflow: hidden;
    background: linear-gradient(90deg, var(--folder-deep), var(--folder-brown) 48%, var(--folder-deep) 50%, var(--folder-brown) 52%, var(--folder-deep));
    font-family: "Didact Gothic", "Century Gothic", sans-serif; color: var(--ink);
  }
  .photo-tile {
    position: absolute;
    background: linear-gradient(160deg, var(--sepia-light), var(--sepia-mid) 60%, var(--sepia-dark));
    border: 2px solid rgba(255,240,220,0.35);
  }
  .spine { position: absolute; left: 599px; top: 0; width: 2px; height: 801px; background: rgba(0,0,0,0.25); }
  .page {
    position: absolute; background: var(--paper);
    box-shadow: 4px 6px 14px rgba(0,0,0,0.55);
  }
  .page--left { left: 60px; top: 88px; width: 454px; height: 605px; }
  .page--right { left: 665px; top: 102px; width: 453px; height: 604px; }
  .brand-mark {
    position: absolute; left: 0; right: 0; top: 48px;
    display: flex; align-items: center; justify-content: center; gap: 8px;
    font-size: 22px; color: var(--brand);
  }
  .brand-mark__dot { width: 16px; height: 16px; border-radius: 50%; background: var(--brand); }
  .body-copy { position: absolute; font-size: 10.3px; line-height: 13.4px; text-align: justify; }
  .page--left .body-copy { left: 58px; top: 130px; width: 339px; }
  .page--right .body-copy { left: 40px; top: 21px; width: 380px; }
  .body-copy p { margin-bottom: 13.4px; }
  .body-copy .list { text-align: left; }
  .pocket {
    position: absolute; left: 704px; top: 604px; width: 496px; height: 197px;
    background: var(--pocket-brown); border-top-left-radius: 46px;
    box-shadow: -2px -3px 8px rgba(0,0,0,0.3);
  }
</style>
</head>
<body>
<main class="spread">
  <div class="photo-tile" style="left:0;top:0;width:160px;height:95px" role="img" aria-label="Sepia photo of a woman relaxing outdoors"></div>
  <div class="photo-tile" style="left:165px;top:0;width:115px;height:88px" role="img" aria-label="Sepia photo of a woman in a mountain landscape"></div>
  <div class="photo-tile" style="left:275px;top:35px;width:130px;height:58px" role="img" aria-label="Sepia photo of two smiling friends"></div>
  <div class="photo-tile" style="left:405px;top:0;width:120px;height:88px" role="img" aria-label="Sepia photo of a young man on a phone"></div>
  <div class="photo-tile" style="left:520px;top:10px;width:80px;height:90px" role="img" aria-label="Sepia photo of a smiling man"></div>
  <div class="photo-tile" style="left:0;top:95px;width:60px;height:100px" role="img" aria-label="Sepia photo of a person outdoors"></div>
  <div class="photo-tile" style="left:0;top:200px;width:60px;height:195px" role="img" aria-label="Sepia portrait of a woman"></div>
  <div class="photo-tile" style="left:0;top:395px;width:60px;height:220px" role="img" aria-label="Sepia photo of a person on a beach"></div>
  <div class="photo-tile" style="left:0;top:620px;width:60px;height:181px" role="img" aria-label="Sepia portrait of a young woman"></div>
  <div class="photo-tile" style="left:50px;top:693px;width:170px;height:108px" role="img" aria-label="Sepia photo of a man with an umbrella"></div>
  <div class="photo-tile" style="left:210px;top:715px;width:190px;height:86px" role="img" aria-label="Sepia photo of a couple walking"></div>
  <div class="photo-tile" style="left:410px;top:693px;width:190px;height:108px" role="img" aria-label="Sepia close-up of a woman in sunglasses"></div>
  <div class="photo-tile" style="left:515px;top:120px;width:85px;height:160px" role="img" aria-label="Sepia portrait of a woman in a headscarf"></div>
  <div class="photo-tile" style="left:515px;top:285px;width:85px;height:220px" role="img" aria-label="Sepia photo of a man at a waterfront"></div>
  <div class="photo-tile" style="left:515px;top:500px;width:85px;height:160px" role="img" aria-label="Sepia photo of a couple by a lake"></div>
  <div class="photo-tile" style="left:600px;top:10px;width:90px;height:190px" role="img" aria-label="Sepia photo of a woman sitting outdoors"></div>
  <div class="photo-tile" style="left:600px;top:215px;width:65px;height:170px" role="img" aria-label="Sepia portrait of a woman"></div>
  <div class="photo-tile" style="left:610px;top:420px;width:55px;height:190px" role="img" aria-label="Sepia portrait of a young woman"></div>
  <div class="photo-tile" style="left:665px;top:0;width:130px;height:100px" role="img" aria-label="Sepia photo of a woman by a lake"></div>
  <div class="photo-tile" style="left:795px;top:0;width:120px;height:100px" role="img" aria-label="Sepia portrait of a smiling woman"></div>
  <div class="photo-tile" style="left:915px;top:0;width:110px;height:100px" role="img" aria-label="Sepia portrait of a young man"></div>
  <div class="photo-tile" style="left:1030px;top:0;width:170px;height:100px" role="img" aria-label="Sepia photo of a man on a phone"></div>
  <div class="photo-tile" style="left:1118px;top:130px;width:82px;height:135px" role="img" aria-label="Sepia portrait of an older man"></div>
  <div class="photo-tile" style="left:1118px;top:265px;width:82px;height:110px" role="img" aria-label="Sepia portrait of a woman"></div>
  <div class="photo-tile" style="left:1118px;top:395px;width:82px;height:200px" role="img" aria-label="Sepia photo of a young woman sitting"></div>

  <div class="spine"></div>

  <section class="page page--left">
    <div class="brand-mark"><span class="brand-mark__dot"></span><span class="brand-mark__name">Northvale Counseling</span></div>
    <div class="body-copy">
      <p>Northvale Counseling is a proactive addiction counseling agency dedicated to address health issues in an integrated manner by working with Pain Management Physicians to offer opiod education to prevent substance use and misuse disorders to their Patients. Northvale Counseling is a resource for Pain Management Clinics to educate and provide prevention and counseling program to patients to reduce the risk of substance use disorders for those patients at risk to pain related substance use disorders.</p>
      <p>Northvale Counseling will provide education and prevention to individuals who are prescribed medications for health related reasons to prevent possible substance use disorders.</p>
      <p>Northvale Counseling will receive referrals from pain management clinics to address this growing issue in healthcare.</p>
      <p>Northvale Counseling services are provided by addiction professionals who are experienced in working in all areas of addiction education and prevention and care.</p>
      <p>Many Pain Management Physicians are interested in reducing risk to their patients and practice from opiod misuse and Increasing Quality Care for their Patients!</p>
      <p>Northvale Counseling will provide education services and screening to provide patients information to reduce the possible addiction potential.</p>
      <p>Northvale Counseling will provide education, prevention, screening, assessments, and referrals for those individuals with chronic pain and substance use disorders.</p>
    </div>
  </section>

  <section class="page page--right">
    <div class="body-copy">
      <p>SERVICES OFFERED<br>
      Pro active opiod education<br>
      Education materials to inform patients about the risk of taking medications inappropriately.<br>
      Prevention services to educate patients about the risk and warning symptoms of substance misuse and abuse<br>
      Screening for potential substance use disorders related to prescribed<br>
      Assessment for substance use disorders related to medical issues and prescribed medications<br>
      Counseling provided by experienced addiction professionals to address substance related misuse and abuse for patients taking prescribed medications.</p>
      <p class="list">Opiod Education<br>Using Opiods safely<br>The Role of Medications<br>Opiod Agreements and Contracts<br>Responsible Use<br>Storing Medication<br>Alcohol &amp; Marijuana and Pain Medication<br>Over the Counter Medication<br>Storing your Medication Safely</p>
      <p>According to the Continental Medical Guild More than 76 million Americans are Suffering with Chronic Pain, Pro Active Addiction Counseling is Needed and No One is Providing This Service!<br>&nbsp;Northvale Counseling Is !</p>
      <p>Northvale's Dedicated Counselors exude a contagious interest in the life of our patients, within an intimately scaled caring environment that engenders transformative learning</p>
      <p>We'er dedicated to informing and educating lives<br>where every patient is treated as a person with individual needs by professional, caring staff</p>
    </div>
  </section>

  <div class="pocket"></div>
</main>
</body>
</html>
```